Upmarket Bathroom and Kitchen ware supplier needs a classy business card design

We are a company based in Fiji, we sell plumbing ware (Kitchen and bathroom taps, Basins,showers, toilets etc) through up market show rooms to individuals and directly through Architects and designers of resorts and holiday houses for new builds and renovations. we are wanting to upgrade our over all look and brand. we are starting with a new logo but will be rebranding the whole business. This project is for a business card design for my management and tales team I would like it to be dark, classy and interesting

Target Market(s)

Resort directors and Management, High end holiday home owners

Contact Information for Business Card

Neil Dawson
Director
+64219473815

Colors

Designer to choose colors to be used in the design.

Requirements
Must have
• Must have an upmarket appearance I like darker charcoal shades but will be guided by the designers
• Please any catch phrases like "Crafting remarkable living rooms" this belongs tpo one of our suppliers so can not be used.
Nice to have
• Double sided, so front dedicated to logo provided and back info about the business and the person.

```html
<!DOCTYPE html>
<html lang="en">
<head>
<meta charset="utf-8">
<title>Lumeria Interiors – Business Card</title>
<link rel="stylesheet" href="https://fonts.googleapis.com/css2?family=Josefin+Sans:wght@300&family=Lato:wght@400&display=swap">
<style>
  :root {
    --backdrop: #3a3a3a;
    --card-dark: #111111;
    --card-light: #f7f7f7;
    --ink-light: #f2f2f2;
    --ink-dark: #141414;
    --rule: #c9c9c9;
  }
  * { margin: 0; padding: 0; box-sizing: border-box; }
  html, body {
    width: 1200px; height: 1015px; overflow: hidden;
    background: var(--backdrop);
  }
  .stage { position: relative; width: 1200px; height: 1015px; }
  .card {
    position: absolute; left: 220px;
    width: 760px; height: 434px;
    box-shadow: 0 14px 30px rgba(0,0,0,.45);
  }
  .card--front { top: 50px; background: var(--card-dark); }
  .card--back  { top: 530px; background: var(--card-light); }

  .brand {
    position: absolute;
    display: flex; flex-direction: column; align-items: center;
    font-family: "Josefin Sans", sans-serif; font-weight: 300;
  }
  .brand__mark {
    width: 74px; height: 74px; border-radius: 50%;
    border: 3px solid currentColor; margin-bottom: 26px;
  }
  .brand__name {
    font-size: 38px; letter-spacing: 14px; line-height: 1;
    padding-left: 14px;
  }
  .brand__rule {
    width: 220px; height: 1px; background: currentColor;
    margin-top: 8px; opacity: .7;
  }
  .brand__sub {
    font-size: 12px; letter-spacing: 6px; margin-top: 8px;
    padding-left: 6px;
  }
  .card--front .brand { color: var(--ink-light); left: 0; right: 0; top: 112px; }
  .card--back .brand  { color: var(--ink-dark); left: 40px; width: 340px; top: 112px; }

  .divider {
    position: absolute; left: 404px; top: 40px; bottom: 40px;
    width: 1px; background: var(--rule);
  }

  .contact {
    position: absolute; left: 440px; top: 80px;
    font-family: "Lato", sans-serif; color: var(--ink-dark);
  }
  .contact__name { font-size: 25px; letter-spacing: .5px; line-height: 1; }
  .contact__role { font-size: 19px; margin-top: 4px; margin-bottom: 14px; }
  .contact__list { list-style: none; }
  .contact__item {
    display: flex; align-items: center; gap: 10px;
    font-size: 19px; line-height: 30px;
  }
  .contact__item svg { width: 17px; height: 17px; flex: none; }
  .contact__address { font-size: 19px; line-height: 26px; margin-top: 14px; }
</style>
</head>
<body>
<main class="stage">

  <section class="card card--front" aria-label="Card front">
    <div class="brand">
      <span class="brand__mark"></span>
      <span class="brand__name">LUMERIA</span>
      <span class="brand__rule"></span>
      <span class="brand__sub">INTERIORS</span>
    </div>
  </section>

  <section class="card card--back" aria-label="Card back">
    <div class="brand">
      <span class="brand__mark"></span>
      <span class="brand__name">LUMERIA</span>
      <span class="brand__rule"></span>
      <span class="brand__sub">INTERIORS</span>
    </div>

    <div class="divider"></div>

    <div class="contact">
      <p class="contact__name">NEIL DAWSON</p>
      <p class="contact__role">Managing Director</p>
      <ul class="contact__list">
        <li class="contact__item">
          <svg viewBox="0 0 16 16" aria-hidden="true"><path fill="#141414" d="M3 1.5l2.5-.5 1.5 3.5-1.8 1.2c.8 1.8 2.3 3.3 4.1 4.1L10.5 8l3.5 1.5-.5 2.5c-.3 1.2-1.4 2-2.6 1.8C6.2 13 3 9.8 2.2 5.1 2 3.9 2.8 1.8 3 1.5z"/></svg>
          000-555 010 100
        </li>
        <li class="contact__item">
          <svg viewBox="0 0 16 16" aria-hidden="true"><rect x="1" y="3" width="14" height="10" rx="1" fill="#141414"/><path d="M1.5 3.8L8 9l6.5-5.2" stroke="#f7f7f7" stroke-width="1.3" fill="none"/></svg>
          info@lumeriainteriors.example
        </li>
        <li class="contact__item">
          <svg viewBox="0 0 16 16" aria-hidden="true"><circle cx="8" cy="8" r="7" fill="#141414"/><path d="M1.5 8h13M8 1.2c-3 3.6-3 10 0 13.6M8 1.2c3 3.6 3 10 0 13.6" stroke="#f7f7f7" stroke-width="1" fill="none"/></svg>
          www.lumeriainteriors.example
        </li>
      </ul>
      <p class="contact__address">14 Harbour Lane, Suva<br>Fiji Islands, 00000</p>
    </div>
  </section>

</main>
</body>
</html>
```